Zaberu - Wordpress website for hot new GIF booth

We need a responsive website for a new brand we're launching. Scrolling parallax style. We are a event photo company offering the hottest new GIF booths. We want our site to be sleek, sexy, moving.

Here's some sites we like:
https://www.tundrix.com/us/
http://kelvasnap.com/
http://lark9.drumvelisaphone.com/

Target Market(s)

advertising agencies, marketing agencies, major brands, corporate planners, millenials

Industry/Entity Type

Events

Number of Pages Required

1 page

Font styles to use
Sans Serif

Colors
33b8a4
86cfc6
ffffff

Requirements
Must have
• I want it very much like this: https://www.tundrix.com/us/
• lots of imagery, movement
• Here's some competitors:
• http://www.quellarix.com/
• http://runbrightwick.com/
• http://www.dqrstudio.com/gif-photo-booth-rental/
• http://kelvasnap.com/
Nice to have
• slider at top with different booth designs
Should not have
• no bulky tabs at top

```html
<!DOCTYPE html>
<html lang="en">
<head>
<meta charset="utf-8">
<title>Zaberu — GIF Booth</title>
<link rel="stylesheet" href="https://fonts.googleapis.com/css2?family=Raleway:wght@300;400;500&family=Open+Sans:wght@400;600&display=swap">
<style>
:root{
  --teal:#33b8a4;
  --teal-soft:#86cfc6;
  --white:#ffffff;
  --ink:#222222;
  --body:#555555;
  --grey-band:#f6f6f6;
  --footer:#000000;
}
*{margin:0;padding:0;box-sizing:border-box}
html,body{width:1200px;height:3482px;overflow:hidden}
body{position:relative;background:var(--white);font-family:"Open Sans",Arial,sans-serif;color:var(--body)}
.abs{position:absolute}

/* header */
.site-header{position:absolute;left:0;top:0;width:1200px;height:135px;border-top:4px solid var(--teal);background:var(--white)}
.brand{position:absolute;left:132px;top:30px;height:72px;display:flex;align-items:center;gap:14px}
.brand-square{width:60px;height:70px;background:var(--ink)}
.brand-name{font-family:"Raleway",sans-serif;font-weight:300;font-size:44px;letter-spacing:2px;color:var(--ink)}
.main-nav{position:absolute;top:64px;left:0;width:1200px;font-family:"Raleway",sans-serif;font-size:12px;font-weight:500;color:var(--ink)}
.main-nav span{position:absolute;white-space:nowrap}
.main-nav .active{color:var(--teal)}

/* hero */
.hero{position:absolute;left:0;top:135px;width:1200px;height:431px;background:linear-gradient(180deg,#35bba7,#2fb09c)}
.hero-title{position:absolute;top:133px;width:1200px;text-align:center;font-family:"Raleway",sans-serif;font-weight:400;font-size:37px;letter-spacing:1px;color:var(--white)}
.hero-sub{position:absolute;top:213px;width:1200px;text-align:center;font-family:"Raleway",sans-serif;font-size:13px;letter-spacing:1px;color:var(--white)}
.hero-btn{position:absolute;left:520px;top:271px;width:158px;height:42px;border:2px solid var(--white);border-radius:21px;color:var(--white);font-family:"Raleway",sans-serif;font-size:13px;text-align:center;line-height:38px}
.hero-arrow{position:absolute;top:177px}

/* features */
.booth-visual{position:absolute;left:150px;top:620px;width:118px;height:396px;
  background:linear-gradient(180deg,#1c1c1c 0%,#262626 9%,#3a3a4a 13%,#f4f4f4 24%,#ffffff 50%,#eeeeee 78%,#2a2a2a 90%,#111 100%);
  clip-path:polygon(20% 0,88% 0,90% 3%,90% 58%,100% 92%,96% 100%,4% 100%,0 96%,10% 60%,18% 58%,18% 3%)}
.feature{position:absolute;width:360px}
.feature-icon{position:absolute;left:0;top:0;width:64px;height:64px;border-radius:50%;background:var(--teal)}
.feature-icon svg{position:absolute;left:16px;top:16px}
.feature h3{position:absolute;left:82px;top:-4px;font-family:"Raleway",sans-serif;font-weight:500;font-size:18px;color:var(--teal);letter-spacing:.5px;white-space:nowrap}
.feature p{position:absolute;left:82px;top:26px;width:268px;font-size:11px;line-height:19px;color:var(--body)}

/* service bands */
.band{position:absolute;left:0;width:1200px}
.band.grey{background:var(--grey-band)}
.band h2{position:absolute;font-family:"Raleway",sans-serif;font-weight:400;font-size:29px;letter-spacing:1px;color:var(--teal);white-space:nowrap}
.band p{position:absolute;width:418px;font-size:11.5px;line-height:19px;text-align:justify;color:var(--body)}
.band .photo{position:absolute;width:414px;height:257px;box-shadow:0 3px 8px rgba(0,0,0,.35)}
.play{position:absolute;left:177px;top:98px}

/* clients */
.clients{position:absolute;left:0;top:3117px;width:1200px;height:151px;background:var(--white)}
.client{position:absolute;top:58px;font-family:"Raleway",sans-serif;font-weight:500;font-size:18px;color:var(--ink);white-space:nowrap}

/* footer */
.site-footer{position:absolute;left:0;top:3268px;width:1200px;height:214px;background:var(--footer)}
.social{position:absolute;top:36px;width:44px;height:44px;border-radius:50%;background:var(--teal)}
.social svg{position:absolute;left:12px;top:12px}
.footer-nav{position:absolute;top:115px;left:0;width:1200px;font-family:"Raleway",sans-serif;font-size:11px;color:var(--white)}
.footer-nav span{position:absolute;white-space:nowrap}
.copyright{position:absolute;top:158px;width:1200px;text-align:center;font-size:10px;color:var(--white);letter-spacing:.5px}
</style>
</head>
<body>

<header class="site-header">
  <div class="brand"><div class="brand-square"></div><div class="brand-name">ZABERU</div></div>
  <nav class="main-nav">
    <span class="active" style="left:448px">THEBOOTH</span>
    <span style="left:557px">PHOTO</span>
    <span style="left:643px">GIF</span>
    <span style="left:708px">VIDEO</span>
    <span style="left:789px">SILENT FILM</span>
    <span style="left:905px">DUB SYNC</span>
    <span style="left:1012px">CONTACT</span>
  </nav>
</header>

<section class="hero" role="img" aria-label="Teal-tinted wall of guest booth portraits behind the slider headline">
  <svg class="hero-arrow" style="left:92px" width="20" height="32" viewBox="0 0 20 32"><path d="M16 2 L4 16 L16 30" fill="none" stroke="#fff" stroke-width="3"/></svg>
  <svg class="hero-arrow" style="left:1088px" width="20" height="32" viewBox="0 0 20 32"><path d="M4 2 L16 16 L4 30" fill="none" stroke="#fff" stroke-width="3"/></svg>
  <h1 class="hero-title">WE COMBINE ART &amp; TECHNOLOGY</h1>
  <div class="hero-sub">LET PEOPLE CREATE &amp; SHARE CONTENT</div>
  <div class="hero-btn">GET STARTED</div>
</section>

<section class="features">
  <div class="booth-visual" role="img" aria-label="Zaberu photo booth kiosk with round screen, ring light and flared base"></div>

  <div class="feature" style="left:339px;top:632px">
    <div class="feature-icon"><svg width="32" height="32" viewBox="0 0 32 32"><rect x="4" y="7" width="24" height="18" fill="none" stroke="#fff" stroke-width="2.5"/><path d="M7 22 L13 15 L18 20 L21 17 L25 22Z" fill="#fff"/><circle cx="21" cy="12" r="2" fill="#fff"/></svg></div>
    <h3>FEATURE RICH</h3>
    <p>Nemo enim ipsam voluptatem quia voluptas sit aspernatur aut odit aut fugit, sed quia consequuntur magni dolores</p>
  </div>
  <div class="feature" style="left:722px;top:632px">
    <div class="feature-icon"><svg width="32" height="32" viewBox="0 0 32 32"><path d="M5 10 H22 V20 A6 6 0 0 1 16 26 H11 A6 6 0 0 1 5 20Z" fill="#fff"/><path d="M22 12 H25 A3 3 0 0 1 25 18 H22" fill="none" stroke="#fff" stroke-width="2.5"/></svg></div>
    <h3>SOCIALLY CONNECTED</h3>
    <p>Nemo enim ipsam voluptatem quia voluptas sit aspernatur aut odit aut fugit, sed quia consequuntur magni dolores</p>
  </div>
  <div class="feature" style="left:339px;top:764px">
    <div class="feature-icon"><svg width="32" height="32" viewBox="0 0 32 32"><path d="M4 15 L28 5 L22 27 L15 20 L24 9 L12 18Z" fill="#fff"/></svg></div>
    <h3>CREATE &amp; SHARE</h3>
    <p>Nemo enim ipsam voluptatem quia voluptas sit aspernatur aut odit aut fugit, sed quia consequuntur magni dolores</p>
  </div>
  <div class="feature" style="left:722px;top:764px">
    <div class="feature-icon"><svg width="32" height="32" viewBox="0 0 32 32"><circle cx="16" cy="9" r="4" fill="#fff"/><circle cx="7" cy="12" r="3" fill="#fff"/><circle cx="25" cy="12" r="3" fill="#fff"/><path d="M9 26 A7 8 0 0 1 23 26Z" fill="#fff"/><path d="M1 25 A6 7 0 0 1 10 19 L8 25Z M31 25 A6 7 0 0 0 22 19 L24 25Z" fill="#fff"/></svg></div>
    <h3>SOCIAL PEOPLE</h3>
    <p>Nemo enim ipsam voluptatem quia voluptas sit aspernatur aut odit aut fugit, sed quia consequuntur magni dolores</p>
  </div>
  <div class="feature" style="left:339px;top:910px">
    <div class="feature-icon"><svg width="32" height="32" viewBox="0 0 32 32"><path d="M4 12 H11 L24 5 V27 L11 20 H4Z" fill="#fff"/><path d="M8 20 L11 28 H14 L12 20Z" fill="#fff"/></svg></div>
    <h3>EXPERIENTIAL MARKETING.</h3>
    <p>Nemo enim ipsam voluptatem quia voluptas sit aspernatur aut odit aut fugit, sed quia consequuntur magni dolores</p>
  </div>
  <div class="feature" style="left:722px;top:910px">
    <div class="feature-icon"><svg width="32" height="32" viewBox="0 0 32 32"><rect x="3" y="9" width="18" height="14" rx="2" fill="#fff"/><path d="M21 14 L29 9 V23 L21 18Z" fill="#fff"/></svg></div>
    <h3>SCALABLE EVENT</h3>
    <p>Nemo enim ipsam voluptatem quia voluptas sit aspernatur aut odit aut fugit, sed quia consequuntur magni dolores</p>
  </div>
</section>

<section class="band grey" style="top:1107px;height:395px">
  <h2 style="left:132px;top:105px">GIF BOOTH</h2>
  <p style="left:132px;top:160px">Neque porro quisquam est, qui dolorem ipsum quia dolor sit amet, consectetur, adipisci velit, sed quia non numquam eius modi tempora incidunt ut labore et dolore magnam aliquam quaerat voluptatem. Ut enim ad minima veniam, quis nostrum exercitationem ullam corporis suscipit laboriosam.</p>
  <div class="photo" style="left:652px;top:68px;background:linear-gradient(160deg,#f3f1ee 0%,#e9e6e2 55%,#b8665a 80%,#e6e3df 100%)" role="img" aria-label="Guest in hat and sunglasses posing under colourful bunting"></div>
</section>

<section class="band" style="top:1502px;height:394px">
  <div class="photo" style="left:134px;top:74px;background:linear-gradient(160deg,#e8e8e6 0%,#dcdad8 50%,#c85a50 80%,#e0dedc 100%)" role="img" aria-label="Guest in paper glasses holding photo props under bunting"></div>
  <h2 style="left:652px;top:110px">SOCIAL PHOTO BOOTH</h2>
  <p style="left:652px;top:164px">Neque porro quisquam est, qui dolorem ipsum quia dolor sit amet, consectetur, adipisci velit, sed quia non numquam eius modi tempora incidunt ut labore et dolore magnam aliquam quaerat voluptatem. Ut enim ad minima veniam, quis nostrum exercitationem ullam corporis suscipit laboriosam.</p>
</section>

<section class="band grey" style="top:1896px;height:397px">
  <h2 style="left:132px;top:106px">SOCIAL STUDIO</h2>
  <p style="left:132px;top:160px">Neque porro quisquam est, qui dolorem ipsum quia dolor sit amet, consectetur, adipisci velit, sed quia non numquam eius modi tempora incidunt ut labore et dolore magnam aliquam quaerat voluptatem. Ut enim ad minima veniam, quis nostrum exercitationem ullam corporis suscipit laboriosam.</p>
  <div class="photo" style="left:652px;top:70px;background:linear-gradient(160deg,#f0f0f0 0%,#bdbdbd 45%,#7a7a7a 70%,#e2e2e2 100%)" role="img" aria-label="Black and white shot of a couple holding a picture frame"></div>
</section>

<section class="band" style="top:2293px;height:425px">
  <div class="photo" style="left:134px;top:89px;background:linear-gradient(160deg,#6a6f78 0%,#3b2f2c 45%,#a8463e 75%,#54585e 100%)" role="img" aria-label="Video still of two friends in big wigs and sunglasses">
    <svg class="play" width="60" height="60" viewBox="0 0 60 60"><circle cx="30" cy="30" r="28" fill="rgba(255,255,255,.35)"/><path d="M24 18 L42 30 L24 42Z" fill="#fff"/></svg>
  </div>
  <h2 style="left:652px;top:118px">SCALABLE EVENT</h2>
  <p style="left:652px;top:172px">Neque porro quisquam est, qui dolorem ipsum quia dolor sit amet, consectetur, adipisci velit, sed quia non numquam eius modi tempora incidunt ut labore et dolore magnam aliquam quaerat voluptatem. Ut enim ad minima veniam, quis nostrum exercitationem ullam corporis suscipit laboriosam.</p>
</section>

<section class="band grey" style="top:2718px;height:399px">
  <h2 style="left:132px;top:116px">CREATE &amp; SHARE CONTENT.</h2>
  <p style="left:132px;top:170px">Neque porro quisquam est, qui dolorem ipsum quia dolor sit amet, consectetur, adipisci velit, sed quia non numquam eius modi tempora incidunt ut labore et dolore magnam aliquam quaerat voluptatem. Ut enim ad minima veniam, quis nostrum exercitationem ullam corporis suscipit laboriosam.</p>
  <div class="photo" style="left:652px;top:72px;background:linear-gradient(160deg,#5a5f66 0%,#2e2a28 45%,#4a4e55 75%,#6b6f75 100%)" role="img" aria-label="Video still of two friends in sunglasses reaching toward the camera">
    <svg class="play" width="60" height="60" viewBox="0 0 60 60"><circle cx="30" cy="30" r="28" fill="rgba(255,255,255,.35)"/><path d="M24 18 L42 30 L24 42Z" fill="#fff"/></svg>
  </div>
</section>

<section class="clients">
  <svg class="abs" style="left:92px;top:55px" width="16" height="30" viewBox="0 0 16 30"><path d="M14 2 L3 15 L14 28" fill="none" stroke="#555" stroke-width="2.5"/></svg>
  <span class="client" style="left:132px">Halverin</span>
  <span class="client" style="left:318px">Corvane Mobile</span>
  <span class="client" style="left:528px">Brisklow</span>
  <span class="client" style="left:660px">Pemberly</span>
  <span class="client" style="left:818px">Ostrand</span>
  <span class="client" style="left:930px">Northmere Goods</span>
  <svg class="abs" style="left:1090px;top:55px" width="16" height="30" viewBox="0 0 16 30"><path d="M2 2 L13 15 L2 28" fill="none" stroke="#555" stroke-width="2.5"/></svg>
</section>

<footer class="site-footer">
  <div class="social" style="left:523px" aria-label="Share"><svg width="20" height="20" viewBox="0 0 20 20"><circle cx="15" cy="4" r="2.6" fill="#fff"/><circle cx="5" cy="10" r="2.6" fill="#fff"/><circle cx="15" cy="16" r="2.6" fill="#fff"/><path d="M15 4 L5 10 L15 16" fill="none" stroke="#fff" stroke-width="1.6"/></svg></div>
  <div class="social" style="left:579px" aria-label="Message"><svg width="20" height="20" viewBox="0 0 20 20"><path d="M2 4 H18 V14 H8 L4 18 V14 H2Z" fill="#fff"/></svg></div>
  <div class="social" style="left:635px" aria-label="Email"><svg width="20" height="20" viewBox="0 0 20 20"><rect x="2" y="5" width="16" height="11" fill="#fff"/><path d="M2 5 L10 11 L18 5" fill="none" stroke="#33b8a4" stroke-width="1.6"/></svg></div>
  <nav class="footer-nav">
    <span style="left:290px">THEBOOTH</span>
    <span style="left:398px">PHOTO</span>
    <span style="left:485px">GIF</span>
    <span style="left:548px">VIDEO</span>
    <span style="left:629px">SILENT FILM</span>
    <span style="left:746px">DUB SYNC</span>
    <span style="left:853px">CONTACT</span>
  </nav>
  <div class="copyright">© 2016 ZABERU.COM &nbsp;THE BEST WEB DESIGNS INSPIRATIONS</div>
</footer>

</body>
</html>
```